Honey Label for 1kg square jar

We require premium looking honey label for 1kg packed in dark amber jar as shown in the image.
Brand is called :"Brindova Honey" - logo to be provided
We would like the following colours to be considered (white, gold and red)
We like to have some flowers and beehives on the background.
The label covers 3 sides of the square jar and were hoping to see render of the front side which should include the brand and also the words" 100% Premium Australian Honey"

Need extra days to review

```html
<!DOCTYPE html>
<html lang="en">
<head>
<meta charset="utf-8">
<title>Brindova Honey – Front Label</title>
<link rel="stylesheet" href="https://fonts.googleapis.com/css2?family=Barlow+Condensed:wght@600;700&display=swap">
<style>
  :root {
    --amber-ground: #3d1511;
    --label-white: #ffffff;
    --stitch-grey: #4a4a4c;
    --brand-red: #5a1f17;
    --honey-gold: #e8b94a;
    --text-grey: #606064;
  }
  * { box-sizing: border-box; margin: 0; padding: 0; }
  html, body {
    width: 1200px;
    height: 1200px;
    overflow: hidden;
  }
  body {
    background: var(--amber-ground);
    font-family: "Barlow Condensed", sans-serif;
  }
  .label {
    position: relative;
    width: 1200px;
    height: 1200px;
  }
  .label-shape {
    position: absolute;
    inset: 0;
  }
  .brand-name {
    position: absolute;
    left: 0;
    width: 1200px;
    text-align: center;
    font-weight: 700;
    color: var(--brand-red);
    text-transform: uppercase;
    line-height: 1;
  }
  .brand-name--main {
    top: 170px;
    font-size: 124px;
    letter-spacing: 2px;
  }
  .brand-name--sub {
    top: 300px;
    font-size: 70px;
    letter-spacing: 10px;
  }
  .emblem {
    position: absolute;
    left: 415px;
    top: 429px;
    width: 370px;
    height: 370px;
    border-radius: 50%;
    border: 10px solid var(--honey-gold);
    background: radial-gradient(circle, #6b2a1e 0%, #8a4a26 38%, #f6e2b0 60%, #fbf1d8 100%);
  }
  .floral-sprig {
    position: absolute;
    top: 505px;
    width: 140px;
    height: 225px;
    border-radius: 70px;
    background: linear-gradient(180deg, #f2cf78 0%, #fbefd0 100%);
  }
  .floral-sprig--left { left: 232px; }
  .floral-sprig--right { left: 828px; }
  .claim {
    position: absolute;
    left: 0;
    width: 1200px;
    text-align: center;
    font-weight: 700;
    text-transform: uppercase;
    line-height: 1;
  }
  .claim--premium {
    top: 828px;
    font-size: 56px;
    color: var(--honey-gold);
    letter-spacing: 1px;
  }
  .claim--origin {
    top: 888px;
    font-size: 46px;
    color: var(--text-grey);
    font-weight: 600;
    letter-spacing: 1px;
  }
  .fill-details {
    position: absolute;
    top: 958px;
    left: 0;
    width: 1200px;
    display: flex;
    justify-content: center;
    align-items: center;
    gap: 16px;
    font-size: 21px;
    font-weight: 600;
    color: var(--text-grey);
    text-transform: uppercase;
  }
  .fill-details .blank {
    display: inline-block;
    width: 62px;
    border-bottom: 4px dotted var(--stitch-grey);
    margin-right: 6px;
    vertical-align: baseline;
  }
  .fill-details .divider {
    width: 2px;
    height: 26px;
    background: var(--text-grey);
  }
</style>
</head>
<body>
  <main class="label">
    <svg class="label-shape" width="1200" height="1200" viewBox="0 0 1200 1200" aria-hidden="true">
      <polygon points="40,600 282,78 918,78 1160,600 918,1122 282,1122" fill="var(--label-white)"/>
      <polygon points="68,600 298,102 902,102 1132,600 902,1098 298,1098"
               fill="none" stroke="var(--stitch-grey)" stroke-width="5" stroke-dasharray="9 9"/>
    </svg>

    <h1 class="brand-name brand-name--main">Brindova</h1>
    <p class="brand-name brand-name--sub">Honey</p>

    <div class="floral-sprig floral-sprig--left" role="img" aria-label="Golden wildflower sprig illustration"></div>
    <div class="emblem" role="img" aria-label="Honey bee on a honeycomb emblem"></div>
    <div class="floral-sprig floral-sprig--right" role="img" aria-label="Golden wildflower sprig illustration"></div>

    <p class="claim claim--premium">100% Premium</p>
    <p class="claim claim--origin">Australian Honey</p>

    <div class="fill-details">
      <span><span class="blank"></span>KG</span>
      <span class="divider"></span>
      <span><span class="blank"></span>Date</span>
    </div>
  </main>
</body>
</html>
```